website design for an energy technology company

Marlow Vektor Holdings is an African based company with interests in renewable energy, clean thermal power and building automation with an overall objective to ensure access to affordable, reliable, sustainable and modern energy for all.
The portal should be simple to navigate. Key attribute is to have scalable pictures of completed projects across the three different portfolios of Renewable energy, thermal power and building automation plus counters on megawatts of electricity.

Target Market(s)

Renewable energy, thermal power, building automation, smart building technology

Industry/Entity Type

Technology Equipment

Coding

Coded - Design and coding required

Number of Pages Required

5+ page

Font styles to use
Sans Serif

Colors
33a6d7
abd037
82c8e6
0255a3
33b8a4

Requirements
Must have
• Photos with human models must feature African males and females at the forefront.
We need counters on the first page and these should be represent installed base for (1) renewables-KW, (2) thermal - (kW), (3) carbon footprint saved
Nice to have
• Would like to have design that is as simple as www.qorbintel.com. With this the left hand roulette style texts will include:
Renewables - This page will now have sub menus on:
Residential Solar
Commercial building solar
Solar Rural Electrification
Windmill
Sustainable technologies

Thermal - will have sub menus like below:
Plant Operation and maintenance
Captive Power Installation

Building Automation - will have sub-menus like:
Commercial building automation
Residential Building Automation
Products
Commercial packages
Services

SDG7 News (connected to the Tz Sustainable development goals)
Blogs
In The News
Should not have
• snow, nuclear power

```html
<!DOCTYPE html>
<html lang="en">
<head>
<meta charset="utf-8">
<title>Marlow Vektor Holdings – Energy Efficiency and Sufficiency</title>
<link href="https://fonts.googleapis.com/css2?family=Montserrat:wght@400;500;600;700&display=swap" rel="stylesheet">
<style>
:root{
  --ink:#232427;
  --dark:#1f2023;
  --footer:#2c2d30;
  --accent:#1ea6cc;
  --white:#ffffff;
  --text:#3b3b3b;
  --muted:#555;
}
*{margin:0;padding:0;box-sizing:border-box}
html,body{width:1200px;height:3103px;overflow:hidden;background:var(--white)}
body{font-family:'Montserrat',sans-serif;color:var(--text);position:relative}
.abs{position:absolute}

/* header */
.site-header{position:absolute;left:0;top:0;width:1200px;height:116px;background:var(--dark)}
.brand{position:absolute;left:102px;top:30px;width:200px;height:56px;display:flex;align-items:center;gap:12px;color:var(--white);font-size:38px;font-weight:600;letter-spacing:4px}
.brand-mark{width:18px;height:18px;border-radius:50%;background:var(--white)}
.main-nav a{position:absolute;top:48px;font-size:15px;color:var(--white);text-decoration:none;font-weight:500}
.main-nav a.active{color:var(--accent)}
.btn-register{position:absolute;left:937px;top:30px;width:146px;height:51px;background:var(--white);color:var(--ink);font-weight:600;font-size:16px;display:flex;align-items:center;justify-content:center;border-radius:2px}

/* hero */
.hero{position:absolute;left:0;top:116px;width:1200px;height:553px;background:linear-gradient(180deg,#b9c4dc 0%,#d9dbe8 30%,#8fb3d3 60%,#2f66b3 80%,#1d4fa0 100%)}
.hero-title{position:absolute;left:341px;top:302px;font-size:36px;font-weight:700;color:#2e3340;letter-spacing:.3px;white-space:nowrap}
.hero-text{position:absolute;left:341px;top:366px;font-size:19px;line-height:35px;color:#2a2e38;font-weight:500;white-space:nowrap}
.btn-start{position:absolute;left:337px;top:446px;width:156px;height:49px;background:var(--white);color:var(--ink);font-weight:600;font-size:17px;display:flex;align-items:center;justify-content:center;border-radius:2px}
.play{position:absolute;left:163px;top:313px}
.slider-dots{position:absolute;left:578px;top:628px;display:flex;gap:8px}
.slider-dots span{width:9px;height:9px;border-radius:50%;background:var(--white)}

/* counters */
.counters{position:absolute;left:337px;top:522px;display:flex;gap:16px}
.counter{width:236px;height:86px;background:rgba(255,255,255,.88);border-radius:3px;border-top:4px solid var(--accent);display:flex;flex-direction:column;align-items:center;justify-content:center;gap:4px}
.counter-value{font-size:26px;font-weight:700;color:var(--accent);line-height:1}
.counter-label{font-size:13px;font-weight:600;color:var(--ink);text-transform:uppercase;letter-spacing:.4px}

/* about */
.section-title{font-weight:700;color:var(--ink);font-size:36px}
.about-title{position:absolute;left:112px;top:758px}
.about-text{position:absolute;left:111px;top:822px;width:537px;font-size:15.4px;line-height:30px;text-align:justify;color:var(--muted)}
.btn-accent{position:absolute;background:var(--accent);color:var(--white);font-weight:700;display:flex;align-items:center;justify-content:center;border-radius:2px}
.btn-more{left:111px;top:1121px;width:145px;height:50px;font-size:17px}
.about-image{position:absolute;left:716px;top:801px}

/* services */
.services{position:absolute;left:0;top:1210px;width:1200px;height:650px}
.services-title{position:absolute;left:0;width:1200px;top:1317px;text-align:center;color:var(--white);font-size:36px;font-weight:700}
.service-card{position:absolute;top:1446px;width:283px;height:202px}
.service-card .shadow{position:absolute;left:-8px;top:-8px;width:297px;height:220px;background:var(--ink);transform:rotate(2deg);border-radius:4px}
.service-card .photo{position:absolute;inset:0;border-radius:3px}
.service-label{position:absolute;top:1696px;width:330px;text-align:center;color:var(--white);font-weight:700;font-size:22px}

/* portfolio */
.portfolio-title{position:absolute;left:0;width:1200px;top:1928px;text-align:center;font-size:40px}
.tile{position:absolute;border:1px solid #d7dde3}
.tile-caption{position:absolute;left:810px;top:2238px;width:258px;height:106px;background:rgba(40,40,40,.55);color:var(--white);font-size:22px;line-height:42px;text-align:center;padding-top:10px;white-space:nowrap}

/* footer */
.site-footer{position:absolute;left:0;top:2596px;width:1200px;height:507px;background:var(--footer)}
.footer-heading{position:absolute;top:2655px;color:var(--white);font-size:31px;font-weight:500}
.contact-icon{position:absolute;left:110px;width:48px;height:48px;border-radius:50%;background:var(--white)}
.contact-text{position:absolute;left:184px;color:var(--white);font-size:19px;line-height:34px}
.field{position:absolute;background:var(--white);border:1px solid #ccc;font-size:18px;color:#444;padding:14px 0 0 31px}
.btn-submit{left:724px;top:2978px;width:148px;height:44px;font-size:21px}
.social span{position:absolute;width:14px;height:14px;border-radius:50%;background:var(--white);top:3020px}
.copyright{position:absolute;left:107px;top:3073px;font-size:13px;color:var(--white)}
</style>
</head>
<body>

<header class="site-header">
  <div class="brand"><span class="brand-mark"></span>MVH</div>
  <nav class="main-nav">
    <a class="active" style="left:402px">HOME</a>
    <a style="left:483px">ABOUT US</a>
    <a style="left:590px">SERVICES</a>
    <a style="left:693px">PORTFOLIO</a>
    <a style="left:811px">CONTACT US</a>
  </nav>
  <div class="btn-register">REGISTER</div>
</header>

<section class="hero" role="img" aria-label="Wind turbines on misty hills above a field of solar panels"></section>
<svg class="play" width="88" height="88" viewBox="0 0 88 88" aria-hidden="true">
  <circle cx="44" cy="44" r="42" fill="#e8eef5" opacity=".8"/>
  <circle cx="44" cy="44" r="35" fill="#fff" stroke="#1ea6cc" stroke-width="6"/>
  <path d="M36 28 L60 44 L36 60 Z" fill="none" stroke="#232427" stroke-width="3" stroke-linejoin="round"/>
</svg>
<h1 class="hero-title">ENERGY EFFICIENCY AND SUFFICIENCY</h1>
<p class="hero-text">Lorem ipsum dolor sit amet, consectetur adipiscing elit,<br>sed do eiusmod tempor incididunt ut labore et dolore magna aliqua.</p>
<div class="btn-start">GET STARTED</div>

<div class="counters">
  <div class="counter"><span class="counter-value">12,500 kW</span><span class="counter-label">Renewables installed</span></div>
  <div class="counter"><span class="counter-value">48,000 kW</span><span class="counter-label">Thermal installed</span></div>
  <div class="counter"><span class="counter-value">36,200 t CO₂</span><span class="counter-label">Carbon footprint saved</span></div>
</div>
<div class="slider-dots"><span></span><span></span><span></span></div>

<h2 class="section-title about-title">ABOUT US</h2>
<p class="about-text">Lorem ipsum dolor sit amet, consectetur adipiscing elit, sed do eiusmod tempor incididunt ut labore et dolore magna aliqua. Quis ipsum suspendisse ultrices gravida. Risus commodo viverra maecenas accumsan lacus vel facilisis. Lorem ipsum dolor sit amet, consectetur adipiscing elit, sed do eiusmod tempor incididunt ut labore et dolore magna aliqua. Quis ipsum suspendisse ultrices gravida. Risus commodo viverra maecenas accumsan lacus vel facilisis. Lorem ipsum dolor sit amet, consectetur adipiscing elit, sed do eiusmod tempor incididunt ut labore et dolore magna aliqua.</p>
<div class="btn-accent btn-more">READ MORE</div>
<svg class="about-image" width="340" height="322" viewBox="0 0 340 322" role="img" aria-label="Wind turbine beside a solar array by a mountain lake">
  <defs><linearGradient id="aboutSky" x1="0" y1="0" x2="0" y2="1"><stop offset="0" stop-color="#7fc3ef"/><stop offset=".55" stop-color="#3d86c9"/><stop offset="1" stop-color="#1d4f8f"/></linearGradient></defs>
  <circle cx="170" cy="160" r="160" fill="#1e73d8"/>
  <circle cx="170" cy="160" r="152" fill="url(#aboutSky)"/>
</svg>

<svg class="services" viewBox="0 0 1200 650" width="1200" height="650" role="img" aria-label="Blue band over wind turbines and solar panels">
  <defs><linearGradient id="bandBlue" x1="0" y1="0" x2="0" y2="1"><stop offset="0" stop-color="#2aaed4"/><stop offset=".6" stop-color="#34b3d6"/><stop offset="1" stop-color="#1f8fc4"/></linearGradient></defs>
  <polygon points="540,30 1200,7 1200,60" fill="#232427"/>
  <polygon points="0,561 0,627 520,600" fill="#232427"/>
  <polygon points="0,17 540,36 1200,60 1200,642 520,600 0,561" fill="url(#bandBlue)"/>
</svg>
<h2 class="services-title">OUR SERVICES</h2>

<div class="service-card" style="left:129px"><div class="shadow"></div><div class="photo" role="img" aria-label="Solar panels and wind turbines near a substation" style="background:linear-gradient(180deg,#6fb0e6,#c9dbee 50%,#2e4f96)"></div></div>
<div class="service-card" style="left:459px"><div class="shadow"></div><div class="photo" role="img" aria-label="Thermal power plant cooling towers at dusk over water" style="background:linear-gradient(180deg,#6b6f8f,#c78d8c 55%,#3e4670)"></div></div>
<div class="service-card" style="left:795px"><div class="shadow"></div><div class="photo" role="img" aria-label="Engineer at a building automation control room" style="background:linear-gradient(135deg,#5fa3b4,#2b5562 55%,#8fa6ae)"></div></div>

<div class="service-label" style="left:105px">RENEWABLE ENERGY</div>
<div class="service-label" style="left:435px">THERMAL POWER</div>
<div class="service-label" style="left:769px">BUILDING AUTOMATION</div>

<h2 class="section-title portfolio-title">PORTFOLIO</h2>
<div class="tile" role="img" aria-label="Person interacting with smart city interface" style="left:111px;top:2050px;width:320px;height:217px;background:linear-gradient(135deg,#4fa9d8,#1b4f82 60%,#c98b55)"></div>
<div class="tile" role="img" aria-label="Power plant with cooling towers lit at dusk" style="left:449px;top:2050px;width:315px;height:217px;background:linear-gradient(180deg,#3c67a8,#7d94b8 50%,#2c3456 75%,#d9a04a)"></div>
<div class="tile" role="img" aria-label="Wind turbine and solar array by a lake" style="left:111px;top:2282px;width:320px;height:217px;background:linear-gradient(180deg,#7ec4ef,#3b84c8 55%,#1c4b8c)"></div>
<div class="tile" role="img" aria-label="Cooling tower silhouetted against an orange night sky" style="left:449px;top:2282px;width:315px;height:217px;background:linear-gradient(180deg,#5a1e0c,#c8520f 60%,#2a0d05)"></div>
<div class="tile" role="img" aria-label="Wind turbines, city towers and rooftop solar panels" style="left:782px;top:2050px;width:306px;height:449px;background:linear-gradient(180deg,#3d8fd6,#b5d6ef 45%,#6b8a6e 62%,#274b8f)"></div>
<div class="tile-caption">INDUSTRIAL AND<br>RESIDENTIAL SOLAR</div>

<footer class="site-footer"></footer>
<h3 class="footer-heading" style="left:110px">Contact Us</h3>
<h3 class="footer-heading" style="left:711px">Get In Touch</h3>

<div class="contact-icon" style="top:2751px"></div>
<svg class="abs" style="left:124px;top:2763px" width="20" height="24" viewBox="0 0 20 24" aria-hidden="true"><path d="M10 1C5 1 2 5 2 9c0 6 8 14 8 14s8-8 8-14c0-4-3-8-8-8z" fill="#1ea6cc"/><circle cx="10" cy="9" r="3" fill="#fff"/></svg>
<p class="contact-text" style="top:2752px">2210 Harbourline<br>Road, Lekki, Lagos</p>

<div class="contact-icon" style="top:2844px"></div>
<svg class="abs" style="left:123px;top:2857px" width="22" height="22" viewBox="0 0 22 22" aria-hidden="true"><path d="M5 2l4 4-2 3c1 3 3 5 6 6l3-2 4 4-3 3C9 20 2 13 2 5z" fill="#1ea6cc"/></svg>
<p class="contact-text" style="top:2850px">Tel:&nbsp; (555) 014-2290</p>

<div class="contact-icon" style="top:2931px"></div>
<svg class="abs" style="left:123px;top:2946px" width="22" height="18" viewBox="0 0 22 18" aria-hidden="true"><rect x="1" y="2" width="20" height="14" rx="2" fill="#1ea6cc"/><path d="M2 3l9 7 9-7" fill="none" stroke="#fff" stroke-width="1.6"/></svg>
<p class="contact-text" style="top:2938px;left:183px">Email:info@mvh-ng.com</p>

<div class="social">
  <span style="left:116px"></span><span style="left:149px"></span><span style="left:188px"></span><span style="left:230px"></span><span style="left:273px"></span>
</div>

<div class="field" style="left:546px;top:2733px;width:243px;height:54px">First Name</div>
<div class="field" style="left:803px;top:2733px;width:244px;height:54px">Last Name</div>
<div class="field" style="left:546px;top:2805px;width:243px;height:53px">Phone</div>
<div class="field" style="left:803px;top:2805px;width:244px;height:53px">Email</div>
<div class="field" style="left:546px;top:2879px;width:501px;height:76px;padding-top:12px">Message</div>
<div class="btn-accent btn-submit">SUBMIT</div>

<p class="copyright">Copyrights © 2020 Copyrights Company Name | All Rights Reserved</p>

</body>
</html>
```